Box design for Jade Roller and gua sha set

Hello I am looking to have a box designed for a Jade Roller and gua sha set. The dimensions have already been Determined. There will be 3 sides with design, 2 sides on the outside with design and 1 on the inside of the box for instructions.

I have attached an Ai file that has the exact dimensions of the box.
I have also attached a few pictures of my product, please find the best way to use them on the box design along with my logos (which I will also attach).

The title of the product is "Jade Roller & Gua Sha Set".

The brand for this product is Brightmoor Goods (please use the logo provided)

I have attached a second logo that says "Wenlowe, Brightmoor Goods...Brightmoor Goods is a part of the Wenlowe Group" Please put this somewhere on the back side of the packaging (preferably at the bottom right corner, small)
Also on the back side please neatly place these features:
SUPERIOR QUALITY: Made from real Jade Stone and developed with high quality materials which result in smooth, noise free rolling
BLOOD CIRCULATION: The Jade Roller has two sides, the bigger side for the general facial area and the smaller side for more accurate massaging around the eyes
ROLL AWAY AGE AND PUFFY DARK EYES: This roller will reduce the dark circles and puffiness around your eyes by circulating blood flow which allows more blood cells to get to places which is difficult without rolling. It will also help reduce the appearance of wrinkles on the forehead with the same method.
GUA SHA TOOL: Included is a Gua Sha tool which is very effective for eye massaging, facial lifting and body scraping
VELVET TRAVEL BAG: Included is also a small carrying bag for the roller and gua sha that tightens

For the inside of the box please insert the instructions photo I have provided. I want to be able to edit the words in this after so please make sure I can do that in adobe.

```html
<!DOCTYPE html>
<html lang="en">
<head>
<meta charset="utf-8">
<title>Jade Roller &amp; Gua Sha Set – Inside Instructions</title>
<link href="https://fonts.googleapis.com/css2?family=Source+Sans+3:wght@400;700&display=swap" rel="stylesheet">
<style>
  :root {
    --paper: #ffffff;
    --ink: #1f1a17;
    --jade: #4ea867;
    --copy-size: 13.6px;
    --copy-leading: 21.6px;
  }
  * { margin: 0; padding: 0; box-sizing: border-box; }
  html, body {
    width: 1200px;
    height: 639px;
    overflow: hidden;
    background: var(--paper);
  }
  .instructions-panel {
    position: relative;
    width: 1200px;
    height: 639px;
    background: var(--paper);
    font-family: "Source Sans 3", "Myriad Pro", Arial, sans-serif;
    font-size: var(--copy-size);
    line-height: var(--copy-leading);
    color: var(--ink);
  }
  .step {
    position: absolute;
  }
  .step h2 {
    font-size: var(--copy-size);
    line-height: var(--copy-leading);
    font-weight: 700;
  }
  .step p {
    text-align: justify;
  }
  .step--care { color: var(--jade); }
  .col-left  { left: 74px;  width: 302px; }
  .col-mid   { left: 446px; width: 310px; }
  .col-right { left: 810px; width: 302px; }
  .step--eyes p, .step--nose p { text-align: left; }
</style>
</head>
<body>
<main class="instructions-panel">
  <section class="step step--care col-left" style="top:47px">
    <h2>Directions:</h2>
    <p>Gently glide the Dual Jade Roller over dean skin 2-3 times daily for 5-10 minutes. The roller is moved with just the weight of the roller pressing the skin. No additional pressure is needed or of benefit. Can be used before application of make up or whilst applying creams to encourage deeper penetration of skincare products.</p>
  </section>

  <section class="step step--care col-left" style="top:243px">
    <h2>Cleaning:</h2>
    <p>Jade can be wiped gently with a soft damp cloth and then dried with an absorbent soft cloth . Its is good to leave it on a cloth or towel for a little while after cleaning to make sure it is completely dry before putting it away. Never wipe Jade with very hot water or soak it in water. Also do not expose Jade to harsh chemicals or deaning agents as it would erode the finish and polish.</p>
  </section>

  <section class="step step--forehead col-left" style="top:459px">
    <h2>Forehead</h2>
    <p>From the center of the forehead moving either left or right begin at the hairline rolling slowly towards the ear. Repeat 3 to 6 times over the same area.</p>
  </section>

  <section class="step step--eyes col-mid" style="top:47px">
    <h2>Eyes</h2>
    <p>Using the small roller, work the lids and under eye area. Continue rolling in in strips from the corner of the eye to the ear with the small roller.</p>
  </section>

  <section class="step step--sinus col-mid" style="top:373px">
    <h2>For sinus pain and pressure</h2>
    <p>Dampen a washcloth and microwave about 10 seconds. Place over your forehead, eyes and cheekbones. Then, starting just above our eyebrows, using the smaller roller, roll from the center of your face as indicaed and continue down to just below your cheekbones.</p>
  </section>

  <section class="step step--nose col-right" style="top:47px">
    <h2>Nose, Lips and chin</h2>
    <p>Using the large roller, work from the nose out to the ear. Continue with upper lip, lower lip and the chin. At the chin follow along the lower jaw line to under the ear lobe. Then repeat with the other side.</p>
  </section>

  <section class="step step--jawline col-right" style="top:395px">
    <h2>Jawline and neck</h2>
    <p>Starting on the chin, work from the center outward and upward on the cheeks Then at the center, make sweeping rolls under the chin towards the collar bone, Working outwards to the sides of the neck.</p>
  </section>
</main>
</body>
</html>
```